Redesign of Medical App for Patients

• The Designer’s task is to provide a new fully-responsive design for our apps, and then code it using only basic html and CSS.
• Your design will be incorporated into our existing REACT native app.

Target Market(s)

Medical Patients

Industry/Entity Type

Medical

Coding

Coded - Design and coding required

Number of Pages Required

5+ page

Requirements
Must have
• Short list candidates will receive detailed briefing
Nice to have
• detailed briefing contains some of our ideas.

```html
<!DOCTYPE html>
<html lang="en">
<head>
<meta charset="utf-8">
<title>CarePath Apps</title>
<link rel="stylesheet" href="https://fonts.googleapis.com/css2?family=Montserrat:wght@400;500;600;700&display=swap">
<style>
  :root {
    --page-bg: #cdeaf6;
    --surface: #ffffff;
    --primary: #1a8fc8;
    --primary-soft: #b6dcf0;
    --ink: #2a2d33;
    --ink-soft: #44474e;
    --link: #1a8fc8;
    --card-rose: #e08b8b;
    --card-periwinkle: #8fa6e0;
    --card-teal: #8ecdc3;
    --art-teal: #8dcdc0;
  }
  * { box-sizing: border-box; margin: 0; padding: 0; }
  html, body { width: 1200px; height: 714px; overflow: hidden; }
  body {
    background: var(--page-bg);
    font-family: "Montserrat", sans-serif;
    color: var(--ink);
    position: relative;
  }
  .board-title {
    position: absolute; left: 63px; top: 50px;
    font-size: 20px; font-weight: 700; color: var(--ink-soft);
  }
  .panel {
    position: absolute; background: var(--surface); overflow: hidden;
  }
  .desktop { left: 63px; top: 103px; width: 829px; height: 539px; border-radius: 17px; }
  .mobile { left: 923px; top: 103px; width: 214px; height: 454px; border-radius: 14px; }
  .abs { position: absolute; }

  .brand { display: flex; align-items: center; gap: 6px; }
  .brand-dot { width: 23px; height: 23px; border-radius: 50%; background: var(--primary); }
  .brand-name { font-size: 14px; font-weight: 600; color: var(--primary); letter-spacing: -0.2px; }

  .nav-item {
    position: absolute; left: 0; display: flex; align-items: center;
    font-size: 8.5px; font-weight: 500; color: var(--ink);
  }
  .nav-item svg { position: absolute; left: 22px; width: 11px; height: 11px; stroke: #666; fill: none; stroke-width: 1.6; }
  .nav-item span { position: absolute; left: 43px; white-space: nowrap; }
  .nav-active-pill {
    position: absolute; left: 0; top: 64px; width: 44px; height: 32px;
    background: var(--primary); border-radius: 0 16px 16px 0;
  }
  .nav-active-pill svg { position: absolute; left: 22px; top: 10px; width: 12px; height: 12px; stroke: #fff; fill: none; stroke-width: 1.6; }

  .hero {
    position: absolute; background: var(--primary); border-radius: 10px; overflow: hidden; color: #fff;
  }
  .hero-art {
    position: absolute;
    background: radial-gradient(ellipse at 50% 55%, #d9913f 0%, #b8743a 35%, #3a4a8c 70%, rgba(26,143,200,0) 100%);
  }
  .hero-kicker { font-size: 11px; font-weight: 600; color: var(--primary-soft); }
  .hero-title { font-weight: 700; line-height: 1.12; }
  .hero-text { font-size: 8.3px; line-height: 1.25; }
  .btn-outline {
    position: absolute; border: 1px solid rgba(255,255,255,0.85); border-radius: 14px;
    display: flex; align-items: center; justify-content: center;
    font-size: 8.3px; color: #fff;
  }

  .section-title { position: absolute; font-size: 11px; font-weight: 600; color: var(--ink); white-space: nowrap; }
  .link-small { position: absolute; font-size: 8.5px; font-weight: 600; color: var(--link); }

  .surgeon-art {
    position: absolute; left: 604px; top: 45px; width: 201px; height: 144px; border-radius: 9px;
    background: linear-gradient(160deg, #95d3c6 0%, var(--art-teal) 55%, #7cc2b5 100%);
  }

  .proc-card { position: absolute; top: 239px; width: 113px; height: 195px; border-radius: 8px; overflow: hidden; }
  .proc-card.rose { background: var(--card-rose); }
  .proc-card.periwinkle { background: var(--card-periwinkle); }
  .proc-card.teal { background: var(--card-teal); }
  .proc-art {
    position: absolute; left: 25px; top: 21px; width: 63px; height: 75px; border-radius: 12px;
    background: radial-gradient(circle at 50% 50%, rgba(255,255,255,0.55), rgba(255,255,255,0) 72%);
  }
  .proc-card.rose .proc-art { background: radial-gradient(circle at 50% 55%, #d4524a 0%, #e07a72 45%, rgba(224,139,139,0) 75%); }
  .proc-card.periwinkle .proc-art { background: radial-gradient(circle at 50% 50%, #f2f3fb 0%, #c4cdf0 45%, rgba(143,166,224,0) 75%); }
  .proc-card.teal .proc-art { background: radial-gradient(circle at 50% 50%, #f6f6f6 0%, #e9a0a0 40%, rgba(142,205,195,0) 75%); }
  .proc-label { position: absolute; top: 110px; left: 0; right: 0; text-align: center; font-size: 8.3px; font-weight: 600; color: #fff; }
  .proc-card .btn-outline { left: 23px; top: 152px; width: 67px; height: 26px; }

  .body-copy { position: absolute; font-size: 8px; line-height: 1.25; color: var(--ink-soft); width: 205px; }

  .care-icon {
    position: absolute; left: 605px; width: 39px; height: 39px; border-radius: 8px; background: var(--primary);
    display: flex; align-items: center; justify-content: center;
  }
  .care-icon svg { width: 20px; height: 20px; fill: none; stroke: #fff; stroke-width: 1.8; stroke-linecap: round; stroke-linejoin: round; }
  .care-name { position: absolute; left: 656px; font-size: 8.5px; font-weight: 600; color: var(--ink); }
  .care-line { position: absolute; left: 656px; font-size: 8px; color: var(--link); }

  .share-bar {
    position: absolute; left: 173px; top: 460px; width: 633px; height: 56px; border-radius: 8px;
    background: var(--surface); box-shadow: 0 2px 10px rgba(30, 80, 120, 0.10);
  }
  .share-label { position: absolute; left: 21px; top: 21px; font-size: 10.5px; font-weight: 500; color: var(--ink); }
  .share-list { position: absolute; left: 75px; top: 14px; display: flex; gap: 14.4px; }
  .share-btn { width: 28px; height: 28px; border-radius: 6px; }

  .settings-icon svg, .icon-line { fill: none; stroke: #666; stroke-width: 1.6; stroke-linecap: round; }

  .tab-bar {
    position: absolute; left: 0; top: 413px; width: 214px; height: 41px; background: var(--surface);
    border-radius: 10px 10px 0 0; box-shadow: 0 -2px 8px rgba(30,80,120,0.06);
  }
  .tab-active { position: absolute; left: 13px; top: 5px; width: 31px; height: 36px; background: var(--primary); border-radius: 16px 16px 0 0; }
  .tab-icon { position: absolute; top: 15px; width: 11px; height: 11px; fill: none; stroke: #666; stroke-width: 1.6; stroke-linecap: round; stroke-linejoin: round; }
  .tab-icon.on { stroke: #fff; }
</style>
</head>
<body>
<svg width="0" height="0" style="position:absolute">
  <defs>
    <symbol id="i-home" viewBox="0 0 24 24"><path d="M3 11l9-7 9 7v9a1 1 0 0 1-1 1h-5v-6H9v6H4a1 1 0 0 1-1-1z"/></symbol>
    <symbol id="i-book" viewBox="0 0 24 24"><path d="M2 5h7a3 3 0 0 1 3 3v12a2 2 0 0 0-2-2H2zM22 5h-7a3 3 0 0 0-3 3v12a2 2 0 0 1 2-2h8z"/></symbol>
    <symbol id="i-clock" viewBox="0 0 24 24"><circle cx="12" cy="12" r="9"/><path d="M12 7v5l3 2"/></symbol>
    <symbol id="i-cal" viewBox="0 0 24 24"><rect x="3" y="5" width="18" height="16" rx="2"/><path d="M3 10h18M8 3v4M16 3v4M7 14h2M11 14h2M15 14h2M7 17h2M11 17h2"/></symbol>
    <symbol id="i-help" viewBox="0 0 24 24"><circle cx="12" cy="12" r="9"/><path d="M9.5 9.5a2.5 2.5 0 1 1 3.5 2.3c-.7.3-1 .8-1 1.5V14M12 17h.01"/></symbol>
    <symbol id="i-check" viewBox="0 0 24 24"><path d="M21 12a9 9 0 1 1-5.3-8.2"/><path d="M8 12l3 3 8-8"/></symbol>
    <symbol id="i-sliders" viewBox="0 0 24 24"><path d="M3 6h18M3 12h18M3 18h18"/><circle cx="8" cy="6" r="2" fill="#fff"/><circle cx="16" cy="12" r="2" fill="#fff"/><circle cx="10" cy="18" r="2" fill="#fff"/></symbol>
  </defs>
</svg>

<h1 class="board-title">CarePath Apps</h1>

<main class="panel desktop">
  <div class="brand abs" style="left:23px;top:21px;">
    <span class="brand-dot"></span><span class="brand-name">CAREPATH</span>
  </div>

  <nav>
    <div class="nav-active-pill"><svg><use href="#i-home"/></svg></div>
    <div class="nav-item" style="top:76px;"><span style="left:52px;">Home</span></div>
    <div class="nav-item" style="top:109px;"><svg><use href="#i-book"/></svg><span style="top:0">Procedures</span></div>
    <div class="nav-item" style="top:142px;"><svg><use href="#i-clock"/></svg><span>Recovery</span></div>
    <div class="nav-item" style="top:176px;"><svg><use href="#i-cal"/></svg><span>At home</span></div>
    <div class="nav-item" style="top:209px;"><svg><use href="#i-help"/></svg><span>What to do if?</span></div>
    <div class="nav-item" style="top:242px;"><svg><use href="#i-check"/></svg><span>Success</span></div>
    <div class="nav-item" style="top:505px;"><svg><use href="#i-sliders"/></svg><span>Settings</span></div>
  </nav>

  <section class="hero" style="left:174px;top:23px;width:399px;height:166px;">
    <div class="hero-art" role="img" aria-label="3D character in a striped sweater taking a selfie with a phone" style="left:21px;top:0;width:133px;height:166px;"></div>
    <p class="hero-kicker abs" style="left:171px;top:17px;">The Patients Guide</p>
    <h2 class="hero-title abs" style="left:171px;top:31px;font-size:19.5px;">Laparoscopic<br>Cholecystectomy</h2>
    <p class="hero-text abs" style="left:171px;top:85px;">Everything you need to know before,<br>during, and after your surgery</p>
    <span class="btn-outline" style="left:171px;top:123px;width:67px;height:26px;">Read more</span>
  </section>

  <h3 class="section-title" style="left:604px;top:22px;">A Message From Your Surgeon</h3>
  <div class="surgeon-art" role="img" aria-label="Illustration of a hand holding a phone with a doctor on video call, surrounded by medical icons"></div>

  <h3 class="section-title" style="left:174px;top:211px;">Procedures</h3>
  <span class="link-small" style="left:529px;top:213px;">Read more</span>

  <article class="proc-card rose" style="left:174px;">
    <div class="proc-art" role="img" aria-label="3D lungs illustration with sparkles"></div>
    <p class="proc-label">About Procedure</p>
    <span class="btn-outline">Read more</span>
  </article>
  <article class="proc-card periwinkle" style="left:318px;">
    <div class="proc-art" role="img" aria-label="3D medical clipboard illustration"></div>
    <p class="proc-label">Pre-Procedure</p>
    <span class="btn-outline">Read more</span>
  </article>
  <article class="proc-card teal" style="left:461px;">
    <div class="proc-art" role="img" aria-label="3D first aid kit illustration"></div>
    <p class="proc-label">Procedure</p>
    <span class="btn-outline">Read more</span>
  </article>

  <h3 class="section-title" style="left:605px;top:211px;">Message To Our Patients</h3>
  <p class="body-copy" style="left:605px;top:239px;">This app will try to help you understand your procedure and how to return to good health.</p>
  <p class="body-copy" style="left:605px;top:268px;">If, at any time, you have questions, or concerns, go immediately to the Emergency Department.</p>

  <h3 class="section-title" style="left:605px;top:315px;">Your Care Team</h3>
  <div class="care-icon" style="top:342px;">
    <svg viewBox="0 0 24 24"><path d="M5 4h4l2 5-2.5 1.5a11 11 0 0 0 5 5L15 13l5 2v4a2 2 0 0 1-2 2A16 16 0 0 1 3 6a2 2 0 0 1 2-2z"/></svg>
  </div>
  <p class="care-name" style="top:343px;">Procedure Physician</p>
  <p class="care-line" style="top:360px;">555-014-2287</p>
  <p class="care-line" style="top:372px;">PhysicianOffice@carepath.example</p>

  <div class="care-icon" style="top:395px;">
    <svg viewBox="0 0 24 24"><path d="M12 21s-7-6.2-7-11a7 7 0 0 1 14 0c0 4.8-7 11-7 11z"/><circle cx="12" cy="10" r="2.5"/></svg>
  </div>
  <p class="care-name" style="top:396px;">Physician’s Office</p>
  <p class="care-line" style="top:412px;">555-014-2287</p>
  <p class="care-line" style="top:424px;">PhysicianOffice@carepath.example</p>

  <div class="share-bar">
    <span class="share-label">Share</span>
    <div class="share-list" aria-label="Share options">
      <span class="share-btn" style="background:#3b6fe0"></span>
      <span class="share-btn" style="background:#4a9ee8"></span>
      <span class="share-btn" style="background:#2d6ea8"></span>
      <span class="share-btn" style="background:#f08a2c"></span>
      <span class="share-btn" style="background:#2d2f36"></span>
      <span class="share-btn" style="background:#c0473a"></span>
      <span class="share-btn" style="background:#5fa12e"></span>
      <span class="share-btn" style="background:#5a8ef0"></span>
      <span class="share-btn" style="background:#e8892c"></span>
      <span class="share-btn" style="background:#b3282d"></span>
      <span class="share-btn" style="background:#e04a5a"></span>
      <span class="share-btn" style="background:#59b843"></span>
      <span class="share-btn" style="background:#4b3de0"></span>
    </div>
  </div>
</main>

<aside class="panel mobile">
  <div class="brand abs" style="left:13px;top:12px;">
    <span class="brand-dot"></span><span class="brand-name">CAREPATH</span>
  </div>
  <svg class="icon-line abs" style="left:189px;top:17px;width:12px;height:12px;"><use href="#i-sliders"/></svg>

  <section class="hero" style="left:13px;top:49px;width:189px;height:281px;">
    <div class="hero-art" role="img" aria-label="3D character in a striped sweater taking a selfie with a phone" style="left:37px;top:9px;width:115px;height:121px;"></div>
    <p class="hero-kicker abs" style="left:12px;top:137px;">The Patients Guide</p>
    <h2 class="hero-title abs" style="left:12px;top:155px;font-size:17px;">Laparoscopic<br>Cholecystectomy</h2>
    <p class="hero-text abs" style="left:12px;top:203px;font-size:8px;">Everything you need to know before,<br>during, and after your surgery</p>
    <span class="btn-outline" style="left:12px;top:239px;width:165px;height:25px;">Read more</span>
  </section>

  <h3 class="section-title" style="left:14px;top:347px;">Procedures</h3>
  <div class="proc-card rose" style="left:14px;top:374px;"><div class="proc-art" role="img" aria-label="3D lungs illustration"></div></div>
  <div class="proc-card periwinkle" style="left:140px;top:374px;"><div class="proc-art" role="img" aria-label="3D medical clipboard illustration"></div></div>

  <nav class="tab-bar">
    <span class="tab-active"></span>
    <svg class="tab-icon on" style="left:23px;"><use href="#i-home"/></svg>
    <svg class="tab-icon" style="left:55px;"><use href="#i-book"/></svg>
    <svg class="tab-icon" style="left:87px;"><use href="#i-clock"/></svg>
    <svg class="tab-icon" style="left:118px;"><use href="#i-cal"/></svg>
    <svg class="tab-icon" style="left:150px;"><use href="#i-help"/></svg>
    <svg class="tab-icon" style="left:181px;"><use href="#i-check"/></svg>
  </nav>
</aside>
</body>
</html>
```